BRAVELO OBSERVATION WHEEL PRODUCT BROCHURE

We need to create a product brochure to showcase our state of the art transportable observation wheel. I have included a rough draft concept with additional pictures to be incorporated into the brochure.

```html
<!DOCTYPE html>
<html lang="en">
<head>
<meta charset="utf-8">
<title>Bravelo Observation Wheel Brochure</title>
<link href="https://fonts.googleapis.com/css2?family=Jost:wght@300;400;600;800&family=Fira+Sans+Condensed:wght@400;600&display=swap" rel="stylesheet">
<style>
  :root {
    --bg: #e8e8e8;
    --paper: #ffffff;
    --navy: #1d1f6e;
    --red: #dc2046;
    --ink: #1a1a1a;
    --muted: #444444;
    --drawing-a: #f4f4f4;
    --drawing-b: #dcdcdc;
    --rule: #cfcfcf;
  }
  * { margin: 0; padding: 0; box-sizing: border-box; }
  html, body { width: 1096px; height: 1200px; overflow: hidden; background: var(--bg); }
  .spread {
    position: absolute; left: 48px; top: 335px;
    width: 1000px; height: 529px;
    background: var(--paper);
    box-shadow: 0 2px 6px rgba(0,0,0,0.08);
  }
  .cover { position: absolute; left: 24px; top: 21px; width: 482px; height: 483px; background: var(--red); }
  .cover-band { position: absolute; left: 0; top: 0; width: 100%; height: 196px; background: var(--navy); }
  .brand {
    position: absolute; left: 43px; top: 107px;
    font-family: "Jost", sans-serif; font-weight: 800; font-size: 38px; letter-spacing: 0.5px;
    color: var(--paper); line-height: 1;
  }
  .tagline {
    position: absolute; left: 43px; top: 149px;
    font-family: "Jost", sans-serif; font-weight: 300; font-size: 23px;
    color: var(--paper); line-height: 1;
  }
  .intro {
    position: absolute; left: 146px; top: 214px; width: 282px;
    font-family: "Fira Sans Condensed", sans-serif; font-weight: 600; font-size: 8px; line-height: 10.5px;
    color: var(--paper);
  }
  .contact {
    position: absolute; left: 146px; top: 291px;
    font-family: "Fira Sans Condensed", sans-serif; font-size: 5.5px; line-height: 7.5px;
    color: var(--paper);
  }
  .contact p + p { margin-top: 8px; }
  .drawing {
    position: absolute; left: 545px; top: 50px; width: 407px; height: 287px;
    border: 1px solid var(--rule);
    background: linear-gradient(135deg, var(--drawing-a), var(--drawing-b));
  }
  .section-title {
    position: absolute;
    font-family: "Jost", sans-serif; font-weight: 800; font-size: 14px; letter-spacing: 0.8px;
    color: var(--ink); line-height: 1;
  }
  .key-title { left: 547px; top: 344px; }
  .tech-title { left: 804px; top: 400px; width: 152px; text-align: right; }
  .features {
    position: absolute; left: 547px; top: 369px; width: 200px;
    display: grid; grid-template-columns: 1fr 1fr; column-gap: 10px;
    font-family: "Fira Sans Condensed", sans-serif; font-size: 6px; line-height: 7.5px; color: var(--muted);
    list-style: none;
  }
  .features ul { list-style: none; }
  .features li { margin-bottom: 8px; }
  .specs {
    position: absolute; top: 428px; left: 680px;
    display: grid; grid-template-columns: 128px 132px; column-gap: 24px;
    font-family: "Fira Sans Condensed", sans-serif; font-size: 6px; color: var(--muted);
  }
  .specs table { border-collapse: collapse; width: 100%; }
  .specs td { padding: 0 0 5.5px; line-height: 6.5px; }
  .specs td:last-child { text-align: right; }
</style>
</head>
<body>
  <main class="spread">
    <section class="cover">
      <div class="cover-band"></div>
      <h1 class="brand">BRAVELO</h1>
      <p class="tagline">ROLLING ACROSS AMERICA</p>
      <p class="intro">The new Giant Wheel is a wonderful attraction for all ages. This wheel is a state of the art stand-alone attraction that will be an instant hit in any city, fair or festival. The concept of the Giant Wheel is considered by many as the one of the greatest inventions of all time. raises the concept to the next level with our unique integrated trailer system</p>
      <div class="contact">
        <p>INFO<br>www.yoursite.com<br>you@yoursite.com<br>(000) 000-0000</p>
        <p>ADDRESS<br>123 Street, City, State</p>
      </div>
    </section>

    <div class="drawing" role="img" aria-label="Technical drawings of the observation wheel: top plan, front and side elevations"></div>

    <h2 class="section-title key-title">KEY CHARACTERISTICS</h2>
    <div class="features">
      <ul>
        <li>• Easy to assemble without the need of a large crane</li>
        <li>• Precision engineering translates to highest safety and operations standards</li>
      </ul>
      <ul>
        <li>• Compact footprint</li>
        <li>• Integrated trailers combine to create the foundation</li>
      </ul>
    </div>

    <h2 class="section-title tech-title">TECHNICAL DETAILS</h2>
    <div class="specs">
      <table>
        <tr><td>• Height</td><td>138ft</td></tr>
        <tr><td>• Wheel Diameter</td><td>74ft</td></tr>
        <tr><td>• Platform Width</td><td>72ft</td></tr>
        <tr><td>• Platform Depth</td><td>57ft</td></tr>
      </table>
      <table>
        <tr><td>• Number of Gondolas</td><td>36</td></tr>
        <tr><td>• Seating capacity per Gondola</td><td>6 passengers</td></tr>
        <tr><td>• Total Seating Capacity</td><td>216 passengers</td></tr>
        <tr><td>• Power Supply</td><td>480/240v 3 phase, 60Hz</td></tr>
      </table>
    </div>
  </main>
</body>
</html>
```